Prospectus/Brochure Design for Partnerships Proposal

Require prospectus to be designed for partnerships packages with our company. The goal of this prospectus is to inspire partners to join Brivel (our company).

Design should be creative and include colour and visual elements to make engaging.

Creativity with layout is encouraged as you see fit.

Company is Brivel.com.au

Contents of brocuhure/prospectus in .pdf. Layout ok to play around with.

Target Market(s)

Startup, Small Business

Industry/Entity Type

Startup

Font styles to use
Sans Serif

Colors

Designer to choose colors to be used in the design.

Requirements
Must have
• Well designed, colour, visual elements, consistency through design with regards to spacing, typography and design elements
Should not have
• Too many colours, select a creative colour pallete and stick with it. Clipart or non vector images.

```html
<!DOCTYPE html>
<html lang="en">
<head>
<meta charset="utf-8">
<title>Brivel Prospectus Cover Spread</title>
<link rel="stylesheet" href="https://fonts.googleapis.com/css2?family=Montserrat:wght@500;600;800&display=swap">
<style>
  :root {
    --stage: #e9e9ea;
    --ink: #1b1b1c;
    --cyan: #0ea5e0;
    --white: #ffffff;
    --photo-crowd-light: #e4e8ee;
    --photo-crowd-dark: #4a5670;
    --photo-meeting-light: #dbe6f1;
    --photo-meeting-dark: #3f5f94;
  }
  html, body {
    margin: 0;
    width: 1200px;
    height: 800px;
    overflow: hidden;
    background: var(--stage);
    font-family: "Montserrat", sans-serif;
  }
  .spread {
    position: absolute;
    left: 80px;
    top: 40px;
    width: 1040px;
    height: 720px;
    box-shadow: 0 18px 40px rgba(0,0,0,0.18);
    overflow: hidden;
  }
  .spread-art { position: absolute; inset: 0; }
  .brand-name {
    font-weight: 800;
    letter-spacing: -0.5px;
    line-height: 1;
    margin: 0;
  }
  .brand-tagline {
    font-weight: 500;
    letter-spacing: 0.3px;
    margin: 4px 0 0 2px;
  }
  .back-cover-brand {
    position: absolute;
    left: 160px;
    top: 440px;
    color: var(--white);
  }
  .back-cover-brand .brand-name { font-size: 38px; }
  .back-cover-brand .brand-tagline { font-size: 10px; }
  .back-cover-contact {
    position: absolute;
    left: 80px;
    top: 515px;
    width: 360px;
    color: var(--white);
    font-size: 10.5px;
    font-weight: 500;
    line-height: 1.6;
    text-align: center;
  }
  .back-cover-contact p { margin: 0; }
  .cover-headline {
    position: absolute;
    left: 505px;
    top: 405px;
    margin: 0;
    color: var(--white);
    line-height: 0.95;
    white-space: nowrap;
    transform: rotate(12deg);
    transform-origin: 0 0;
  }
  .headline-lead { display: block; font-weight: 600; font-size: 24px; }
  .headline-main { display: block; font-weight: 800; font-size: 46px; letter-spacing: -1px; }
  .headline-tail { display: block; font-weight: 600; font-size: 20px; margin-top: 4px; }
  .front-cover-brand {
    position: absolute;
    right: 24px;
    top: 600px;
    color: var(--white);
    text-align: right;
  }
  .front-cover-brand .brand-name { font-size: 54px; }
  .front-cover-brand .brand-tagline { font-size: 12px; }
</style>
</head>
<body>
<main class="spread">
  <svg class="spread-art" width="1040" height="720" viewBox="0 0 1040 720">
    <defs>
      <linearGradient id="crowd-tone" x1="0" y1="0" x2="1" y2="1">
        <stop offset="0" stop-color="var(--photo-crowd-light)"/>
        <stop offset="0.6" stop-color="var(--photo-crowd-dark)"/>
        <stop offset="1" stop-color="var(--photo-crowd-light)"/>
      </linearGradient>
      <linearGradient id="meeting-tone" x1="0" y1="0" x2="1" y2="1">
        <stop offset="0" stop-color="var(--photo-meeting-light)"/>
        <stop offset="0.55" stop-color="#a9bfd8"/>
        <stop offset="1" stop-color="var(--photo-meeting-dark)"/>
      </linearGradient>
    </defs>
    <rect class="photo-crowd" x="0" y="0" width="520" height="420" fill="url(#crowd-tone)" role="img" aria-label="Photo of business people walking through a busy city lobby"/>
    <rect class="photo-meeting" x="520" y="0" width="520" height="720" fill="url(#meeting-tone)" role="img" aria-label="Photo of colleagues meeting around a table in a bright coworking office"/>
    <polygon class="accent-triangle-back" points="300,140 0,368 330,372" fill="var(--cyan)"/>
    <polygon class="dark-panel" points="0,385 340,395 360,352 600,330 860,720 0,720" fill="var(--ink)" stroke="var(--white)" stroke-width="4"/>
    <polygon class="accent-triangle-front" points="740,520 1040,450 1040,720 860,720" fill="var(--cyan)" stroke="var(--white)" stroke-width="4"/>
  </svg>

  <div class="back-cover-brand">
    <p class="brand-name">Brivel</p>
    <p class="brand-tagline">empower. achieve. succeed.</p>
  </div>
  <div class="back-cover-contact">
    <p>02 5550 1842 &nbsp;|&nbsp; info@brivel.com.au &nbsp;|&nbsp; brivel.com.au</p>
    <p>14 Harbourline St, Redfern Vale, NSW, 2016</p>
  </div>

  <h1 class="cover-headline">
    <span class="headline-lead">Coworking</span>
    <span class="headline-main">Spaces</span>
    <span class="headline-main">Don’t Get</span>
    <span class="headline-tail">Much Better Than This</span>
  </h1>

  <div class="front-cover-brand">
    <p class="brand-name">Brivel</p>
    <p class="brand-tagline">empower. achieve. succeed.</p>
  </div>
</main>
</body>
</html>
```